Business Card Design

We have our logo and everything in place. Looking to have a layout for our new business cards designed. These will be printed with a matte finish, possibly rounded corners, and looking to incorporate some cool spot UV layers into the design.

Ive uploaded the existing card front and back as well as our logo.

Card Size Will Be 3.5" x 2"

Industry/Entity Type

Business

```html
<!DOCTYPE html>
<html lang="en">
<head>
<meta charset="utf-8">
<title>Summit Porch &amp; Fence – Business Cards</title>
<link rel="stylesheet" href="https://fonts.googleapis.com/css2?family=Open+Sans:wght@400;600&display=swap">
<style>
  :root {
    --backdrop: #4a403b;
    --card: #1c1c1d;
    --card-edge: #262627;
    --ink: #f4f4f4;
    --ink-soft: #d9d9d9;
    --accent: #2f8fd8;
    --rule: #8a8a8a;
  }
  * { box-sizing: border-box; margin: 0; padding: 0; }
  html, body {
    width: 1200px; height: 780px; overflow: hidden;
    background: var(--backdrop);
    font-family: "Open Sans", Arial, sans-serif;
  }
  .canvas { position: relative; width: 1200px; height: 780px; }

  .card {
    position: absolute;
    width: 540px; height: 309px;
    background: var(--card);
    border: 1px solid var(--card-edge);
    border-radius: 6px;
    box-shadow: 0 14px 30px rgba(0,0,0,.45);
    color: var(--ink);
  }
  .card--front { left: 50px; top: 90px; }
  .card--back  { left: 610px; top: 380px; }

  .wordmark {
    font-weight: 400;
    color: var(--ink);
    text-align: center;
    line-height: 1.15;
    letter-spacing: .5px;
  }
  .card--front .wordmark {
    position: absolute; left: 0; right: 0; top: 118px;
    font-size: 34px;
  }
  .card--back .wordmark {
    position: absolute; left: 20px; width: 250px; top: 112px;
    font-size: 27px;
  }

  .divider {
    position: absolute; left: 290px; top: 80px;
    width: 1px; height: 150px; background: var(--rule);
  }

  .contact-block { position: absolute; left: 312px; top: 92px; }
  .person-name {
    font-weight: 600; font-size: 21px; letter-spacing: .5px;
    text-transform: uppercase; line-height: 1.1;
  }
  .person-title { color: var(--accent); font-size: 15px; margin-top: 1px; }

  .contact-list { list-style: none; margin-top: 34px; }
  .contact-list li {
    display: flex; align-items: center; gap: 7px;
    font-size: 14px; color: var(--ink-soft); line-height: 22px;
  }
  .contact-icon { width: 15px; height: 15px; flex: none; }
</style>
</head>
<body>
<main class="canvas">

  <section class="card card--front" aria-label="Card front">
    <p class="wordmark">Summit Porch &amp; Fence</p>
  </section>

  <section class="card card--back" aria-label="Card back">
    <p class="wordmark">Summit Porch &amp; Fence</p>
    <div class="divider"></div>
    <div class="contact-block">
      <h1 class="person-name">Daniel Mercer</h1>
      <p class="person-title">President</p>
      <ul class="contact-list">
        <li>
          <svg class="contact-icon" viewBox="0 0 16 16" aria-hidden="true">
            <rect width="16" height="16" rx="2" fill="var(--accent)"/>
            <path d="M5 3.5 L7 5.5 L6 7 Q7.5 9 9 10 L10.5 9 L12.5 11 L11 12.5 Q6 11.5 3.5 5 Z" fill="#fff"/>
          </svg>
          403.555.0187
        </li>
        <li>
          <svg class="contact-icon" viewBox="0 0 16 16" aria-hidden="true">
            <rect width="16" height="16" rx="2" fill="var(--accent)"/>
            <rect x="3" y="4.5" width="10" height="7" fill="none" stroke="#fff" stroke-width="1.2"/>
            <path d="M3 4.5 L8 8.5 L13 4.5" fill="none" stroke="#fff" stroke-width="1.2"/>
          </svg>
          hello@summitporchfence.com
        </li>
        <li>
          <svg class="contact-icon" viewBox="0 0 16 16" aria-hidden="true">
            <rect width="16" height="16" rx="2" fill="var(--accent)"/>
            <circle cx="8" cy="8" r="4.8" fill="none" stroke="#fff" stroke-width="1.1"/>
            <ellipse cx="8" cy="8" rx="2" ry="4.8" fill="none" stroke="#fff" stroke-width="1"/>
            <path d="M3.2 8 H12.8" stroke="#fff" stroke-width="1"/>
          </svg>
          www.summitporchfence.com
        </li>
      </ul>
    </div>
  </section>

</main>
</body>
</html>
```